Healthcare Recruitment Agency Brochure

We need our current Brochure updated as its old and dated. The brochure will be for our current and potential Clients and should provide all the necessary information regarding our services, but in a well presented, easy reading format which echoes our company Brand. The company supplies Healthcare establishments with trained healthcare Staff which can be in a variety of settings.
UPDATE: Following the submission of many designs we would like to amend the information/content to be included in the brochure and have uploaded additional information. We would like an 8 page booklet with the various sections spread out so as not to look to 'wordy' page 1 Front cover, 2 About Us, 3 Our Service, 4 Our promise, 5 Our Staff, 6 Our Ethos, 7 What Our Clients Say/Testimonials, 8 Contact Us/Back page. Please if using pictures (which is welcomed) steer away from the surgical/doctor type. We mainly provide care to the Elderly within Nursing and Residential Homes and Support Environments. Thanks

Target Market(s)

Healthcare clientell

Industry/Entity Type

Healthcare

Requirements
Must have
• Pictures, animation, easy reading, informative, tie in with website theme www.silverbrooknursingteam.co.uk
Nice to have
• open to ideas
Should not have
• very long text paragraphs

```html
<!DOCTYPE html>
<html lang="en">
<head>
<meta charset="utf-8">
<title>Silverbrook Nursing Brochure</title>
<link href="https://fonts.googleapis.com/css2?family=Oswald:wght@500;600&family=Lato:wght@400;700&display=swap" rel="stylesheet">
<style>
  :root{
    --backdrop:#e4e5e7;
    --paper:#ffffff;
    --blue:#2b5cab;
    --teal:#1fb8a0;
    --ink:#3a3a3a;
    --muted:#6b6b6b;
    --rule:#555;
  }
  *{box-sizing:border-box;margin:0;padding:0}
  html,body{width:1200px;height:1200px;overflow:hidden}
  body{background:var(--backdrop);font-family:'Lato',sans-serif;color:var(--ink);position:relative}
  .spread{position:absolute;left:180px;top:17px;display:grid;grid-template-columns:400px 400px;grid-template-rows:566px 566px;gap:34px 40px}
  .page{background:var(--paper);position:relative;box-shadow:0 2px 8px rgba(0,0,0,.12);overflow:hidden}
  .heading{font-family:'Oswald',sans-serif;font-weight:600;color:var(--blue);text-transform:uppercase;text-align:center;letter-spacing:.3px}
  .heading--main{font-size:12px;margin-bottom:10px}
  .heading--sub{font-size:8.5px;color:#333;margin-bottom:5px}
  .body-text{font-size:6.6px;line-height:1.5;margin-bottom:8px;text-align:justify}
  .body-text b{font-weight:700}
  .hl{color:var(--blue)}
  .tag{background:var(--teal);color:#fff;padding:0 2px}
  .brand{font-family:'Lato',sans-serif;font-weight:700;color:var(--blue);display:flex;align-items:center;gap:8px}
  .brand__dot{width:12px;height:12px;border-radius:50%;background:var(--teal);flex:none}
  .photo{border-radius:0}

  /* cover */
  .cover{border:1px solid #777}
  .cover__brand{position:absolute;left:24px;top:24px;font-size:21px}
  .cover__photo{position:absolute;left:0;top:94px;width:100%;height:268px;background:linear-gradient(160deg,#6f8f55 0%,#9ab36d 40%,#c9704f 70%,#8d9a78 100%)}
  .cover__pills{position:absolute;left:20px;right:20px;top:408px;display:flex;justify-content:space-between}
  .pill{width:106px;height:22px;background:var(--teal);border:2px solid #fff;outline:1px solid var(--teal);color:#fff;font-family:'Oswald',sans-serif;font-weight:500;font-size:7px;text-transform:uppercase;display:flex;align-items:center;justify-content:center}

  /* about */
  .about{padding:70px 26px 0}
  .about .heading--main{margin-bottom:12px}
  .about .vision{margin-top:16px}
  .signature{font-family:'Oswald',sans-serif;font-weight:500;font-size:8px;margin-top:4px}
  .about__foot{position:absolute;left:26px;right:26px;top:452px;height:80px;display:flex;justify-content:space-between;align-items:center}
  .about__faint{font-size:24px;color:#e4ebf4}
  .about__photo{width:60px;height:80px;background:linear-gradient(180deg,#dfe8ee,#a9c3d6)}

  /* why us */
  .why{padding:26px 26px 0}
  .why__top{display:grid;grid-template-columns:1fr 90px;gap:14px;margin-top:2px}
  .why__top .photo{height:90px;background:linear-gradient(160deg,#7a9a55,#a7b7c8 60%,#b88a70)}
  .why__cols{display:grid;grid-template-columns:1fr 1fr;gap:22px;margin-top:10px}
  .why__cols .body-text{font-size:6.3px}
  .why__photo{margin:4px 20px 0;height:150px;background:linear-gradient(120deg,#a77e66 0%,#d8c3b0 45%,#f0f0f0 70%,#c9b49a 100%)}

  /* back */
  .back{padding:64px 26px 0}
  .back .intro{text-align:center;font-size:6.6px;line-height:1.5;margin-bottom:8px}
  .offer{display:grid;grid-template-columns:1fr 1fr;gap:6px 20px;width:220px;margin:0 auto 26px;font-size:6px}
  .offer li{list-style:none;display:flex;align-items:center;gap:5px}
  .offer svg{flex:none}
  .branches{background:var(--teal);color:#fff;display:grid;grid-template-columns:1fr 1fr;gap:22px 20px;padding:8px 10px 12px;font-size:6px;line-height:1.45;margin-bottom:16px}
  .reach{text-align:center;font-size:6.4px;line-height:1.6}
  .back__brand{justify-content:center;font-size:22px;margin-top:22px}
</style>
</head>
<body>
<main class="spread">

  <section class="page cover">
    <div class="brand cover__brand"><span class="brand__dot"></span>Silverbrook Nursing</div>
    <div class="photo cover__photo" role="img" aria-label="Photo of a smiling carer standing behind an elderly woman in a wheelchair in a garden"></div>
    <div class="cover__pills">
      <span class="pill">Officially Recognised</span>
      <span class="pill">Simplicity</span>
      <span class="pill">Superior Solutions</span>
    </div>
  </section>

  <section class="page about">
    <h2 class="heading heading--main">About Us</h2>
    <p class="body-text">With over 20 years experience in the industry, <span class="hl">Silverbrook Nursing</span> specialises in temporary staffing solutions for the healthcare sector. We <b>recruit</b> for various positions including Healthcare Assistants, Support Workers and Registered Nurses to work flexible hours with our clients at times to suit. We currently have a <b>branch network</b> throughout Kent and East Sussex with expansion plans to become one of the largest UK providers of Healthcare professionals.</p>
    <p class="body-text">As a <span class="hl">validated member of the NSRA</span> (National Staffing &amp; Recruitment Association) you can rest assured that we will always be working in line with current legislation and guidelines, offering a seamless registration process for all staff. We strive for excellence in every aspect of our service and this includes ensuring that we are always fair, honest and supportive of our clients and staff members.</p>
    <p class="body-text">As a company, we implement our core values wherever possible in everything that we do:</p>
    <p class="body-text"><span class="tag">Honesty and Integrity</span> We pride ourselves on being direct and straightforward when communicating with our clients and candidates.</p>
    <p class="body-text"><span class="tag">Dedication</span> Our consultants aim to fully understand the requirements of our clients and candidates to find mutually beneficial solutions.</p>
    <p class="body-text"><span class="tag">Service Excellence</span> We aim to always deliver superior services to help both employers and candidates achieve their goals.</p>
    <p class="body-text"><span class="tag">Leadership</span> Our purpose is to become leaders in the healthcare recruitment sector, raising the bar for the entire industry.</p>
    <h2 class="heading heading--sub vision">Our Vision</h2>
    <p class="body-text">We aim to thrive as a business by enriching the lives of our employees and service users through our commitment to excellence. Our team enables healthcare workers to advance their careers while providing local establishments with a quality, affordable staffing solution to meet a variety of requirements.</p>
    <p class="signature">– Mark Ellison / Managing Director</p>
    <div class="about__foot">
      <div class="brand about__faint">Silverbrook Nursing</div>
      <div class="photo about__photo" role="img" aria-label="Photo of a group of care staff in uniforms"></div>
    </div>
  </section>

  <section class="page why">
    <h2 class="heading heading--main">Why Us</h2>
    <div class="why__top">
      <div>
        <h3 class="heading heading--sub">Our Mission</h3>
        <p class="body-text">We aim to provide simple, straightforward recruitment services for healthcare facilities throughout Kent. Our agency makes the booking process easy and affordable for all our clients and we ensure that the application process is clear and uncomplicated for potential candidates. It is our goal to become the agency of choice, setting the standards for temporary and permanent healthcare recruitment.</p>
      </div>
      <div class="photo" role="img" aria-label="Photo of a carer walking with an elderly man in a wheelchair outdoors"></div>
    </div>
    <div class="why__cols">
      <div>
        <h3 class="heading heading--sub">Our Expertise</h3>
        <p class="body-text">With over 20 years of experience within the industry, Silverbrook Nursing specialises in reliable recruitment solutions for the Healthcare sector. Supporting a wide range of healthcare establishments with varied staffing requirements, our team has the extensive capability to deliver service excellence. We're here to exceed client expectations and offer a superior care service.</p>
      </div>
      <div>
        <h3 class="heading heading--sub">Our Approach</h3>
        <p class="body-text">We are committed to delivering a service superior to those of our competitors and we do this by keeping our core values at the heart of all we do. We recognise that in order to maintain a happy and reliable work force we need our pay structure to reflect hard work and dedication. Our pay scale is competitive and we acknowledge all staff achievements allowing us to maintain a high level of service for all our clients.</p>
      </div>
    </div>
    <div class="photo why__photo" role="img" aria-label="Photo of a carer laughing with an elderly woman indoors"></div>
  </section>

  <section class="page back">
    <h2 class="heading heading--sub">What We Have To Offer</h2>
    <p class="intro">We are proud to work with a diverse range of clients and train our staff accordingly giving them the opportunity to excel in each area. Please click on each category below for more information.</p>
    <ul class="offer">
      <li><svg width="9" height="9" viewBox="0 0 10 10"><path d="M2 5.2l2 2 4-4.4" fill="none" stroke="#2b5cab" stroke-width="1.4"/></svg>Residential Homes</li>
      <li><svg width="9" height="9" viewBox="0 0 10 10"><path d="M2 5.2l2 2 4-4.4" fill="none" stroke="#2b5cab" stroke-width="1.4"/></svg>Support Work</li>
      <li><svg width="9" height="9" viewBox="0 0 10 10"><path d="M2 5.2l2 2 4-4.4" fill="none" stroke="#2b5cab" stroke-width="1.4"/></svg>Hospitals</li>
      <li><svg width="9" height="9" viewBox="0 0 10 10"><path d="M2 5.2l2 2 4-4.4" fill="none" stroke="#2b5cab" stroke-width="1.4"/></svg>Nursing Homes</li>
    </ul>
    <h2 class="heading heading--sub">Our Braches</h2>
    <div class="branches">
      <p>LARCHFORD | KENT<br>14 Mill Lane, Larchford, Kent,<br>LF2 4QD<br>Tel: 01632 960 211</p>
      <p>ELMSBURY | KENT<br>3 Orchard Court, Abbey Rise,<br>Elmsbury, Kent, EB1 7HN<br>Tel: 01632 960 354</p>
      <p>RIVERTON | KENT<br>6 Weaver Place, Riverton, Kent,<br>RV4 2AX<br>Tel: 01632 960 418</p>
      <p>OAKBRIDGE | KENT<br>118 Meadow Road, Oakbridge,<br>OB9 3LT<br>Tel: 01632 960 587</p>
    </div>
    <h2 class="heading heading--sub">Reach Us</h2>
    <p class="reach">www.silverbrooknursingteam.co.uk<br>info@silverbrooknursingteam.co.uk<br>+44 1632 960418</p>
    <div class="brand back__brand"><span class="brand__dot"></span>Silverbrook Nursing</div>
  </section>

</main>
</body>
</html>
```